Flyer für dynamisches Maklerteam
The design process with Brightwing went very well. He responded precisely to our requirements and to our target group and developed designs that reflect our logo and our corporate identity in many small details. Communication with Brightwing went great. He quickly translated our requests into wonderful designs and created flyers that we are very happy with. Brightwing is a good designer and I can highly recommend working with him. Dr. Ilse Brandvoort KORVEN Real Estate
Zielgruppe
KORVEN Immobilien ist ein dynamisches Maklerteam, dass sich auf den Verkauf von Wohnimmobilien des gehobenen Preissegmentes spezialisiert hat. Unser Schwerpunkt liegt auf Luxusobjekten.
Hallo,
schön, dass ihr an unserem Design-Wettbewerb teilnehmt.
Unser Zielgruppe sind verkaufswillige Eigentümer hochpreisiger Immobilien.
--> eine ganz wichtige Kundengruppe sind Erben, die ihre geerbte Immobilie verkaufen wollen.
Wir wünschen uns beidseitig bedruckte Flyer auf hochwertigem Material (Chromosulfatpapier, 450 g/m²). Bei der Auswahl des Formates wollen wir euch freie Hand lassen.
Vorderseite:
- Logo von KORVEN Immobilien.
- Ein Foto als Eye-Catcher, das Interesse weckt, zum Schmunzeln bringt und in Erinnerung bleibt. Wichtig: Auf dem Foto sollte man Freude sehen (gerne lächelnde Gesichter, die Personen müssen nicht zwangsläufig in die Kamera blicken. Eine positive und glückliche Grundstimmung auf dem Bild ist wichtig). -> an dieser Stelle bitte geeignete Stock-Bilder recherchieren und diese vorschlagen.
- Claim: Genießen Sie Ihre Freiheit. Wir verkaufen Ihre Immobilie.
Rückseite:
folgenden Text bitte verwenden:
Das Besondere bei KORVEN Immobilien:
- langjährige Erfahrung mit Immobilien des gehobenen Segments
- hochprofessionelle Komplettabwicklung in kürzester Zeit
- ausgezeichnete Referenzen
- auf Wunsch sehr diskrete Abwicklung
Anschließend bitte einen Satz, der eine Abschlussfrage formuliert, die etwa folgenden Inhalt wiedergibt:
'Wenn Sie direkt mit uns sprechen möchten, erreichen Sie uns jederzeit unter 0157 - 3948 2036.'
(Diesen Satz könnt ihr gerne umformulieren.)
Website und Emailadresse [ www.korven-immobilien.example - ib@korven-immobilien.example ]
Bilder des gesamten KORVEN Verkaufsteam als Einzelportraits vor dunklem Hintergrund.
Dabei wichtig: Lorenz Korven als Chef bitte an die erste Stelle setzen. Henrike und Jonas Weidlich sind ein Ehepaar, die Immobilien meist gemeinsam verkaufen, daher bitte auch ihre beiden Portraits nebeneinander platzieren.
Bei der Gestaltung des Flyers i..

```html
<!DOCTYPE html>
<html lang="de">
<head>
<meta charset="utf-8">
<title>KORVEN Immobilien – Flyer</title>
<link rel="stylesheet" href="https://fonts.googleapis.com/css2?family=Jost:wght@400;500;700&family=Marcellus+SC&display=swap">
<style>
  :root {
    --stage: #ececec;
    --navy: #2b3470;
    --navy-deep: #232a5c;
    --gold: #a88a5c;
    --gold-light: #c9a86e;
    --paper: #ffffff;
    --light-band: #e9e9ec;
    --team-dark: #25252b;
    --text-light: #eef0f8;
  }
  * { box-sizing: border-box; margin: 0; padding: 0; }
  html, body { width: 1200px; height: 2400px; overflow: hidden; background: var(--stage); }
  body { position: relative; font-family: "Jost", sans-serif; }

  .flyer-pair { position: absolute; left: 250px; width: 700px; height: 480px; display: flex; gap: 20px; }
  .flyer-pair--one { top: 160px; }
  .flyer-pair--two { top: 960px; }
  .flyer-pair--three { top: 1760px; }

  .flyer { position: relative; width: 340px; height: 480px; background: var(--paper); overflow: hidden;
           box-shadow: 0 14px 30px rgba(0,0,0,.12); }

  /* back side */
  .back__photo { position: absolute; left: 0; top: 0; width: 340px; height: 115px;
                 background: linear-gradient(180deg, #6f9a5a 0%, #8fae78 40%, #d9dcd8 62%, #6d6c6a 100%); }
  .gold-band { position: absolute; left: 0; width: 100%; height: 14px;
               background: linear-gradient(90deg, var(--gold), var(--gold-light), var(--gold)); }
  .back .gold-band { top: 115px; }
  .back__benefits { position: absolute; left: 0; top: 129px; width: 340px; height: 203px; background: var(--navy);
                    padding: 22px 22px 0 44px; color: var(--text-light); }
  .badge { position: absolute; right: 14px; top: 80px; width: 74px; height: 74px; border-radius: 50%;
           background: var(--navy); border: 3px solid #fff; box-shadow: 0 2px 6px rgba(0,0,0,.3);
           display: flex; flex-direction: column; align-items: center; justify-content: center;
           font-size: 7px; font-weight: 700; line-height: 1.25; text-align: center; z-index: 2; }
  .badge__top { color: #fff; }
  .badge__sub { color: var(--gold-light); }
  .benefits__title { font-family: "Marcellus SC", serif; font-size: 13px; line-height: 1.1; color: #fff; font-weight: 400; }
  .benefits__title span { display: block; color: var(--gold-light); }
  .benefit-list { list-style: none; margin: 8px 0 10px; }
  .benefit-list li { display: flex; align-items: center; gap: 6px; font-size: 7px; line-height: 1; margin-bottom: 6px; }
  .benefit-list svg { width: 9px; height: 9px; flex: none; }
  .benefits__text { font-size: 6px; line-height: 1.75; color: var(--text-light); padding-right: 4px; }

  .back__contact { position: absolute; left: 0; top: 332px; width: 340px; height: 63px; background: var(--light-band);
                   padding: 9px 16px 0 80px; color: var(--navy); }
  .contact__lead { font-size: 6.5px; font-weight: 500; }
  .contact__phone { font-size: 14px; font-weight: 700; margin: 2px 0 3px 40px; letter-spacing: .3px; }
  .contact__lines { display: flex; gap: 10px; font-size: 6px; font-weight: 500; }
  .contact__lines span { display: flex; align-items: center; gap: 3px; }
  .contact__lines svg { width: 8px; height: 8px; }

  .back__team { position: absolute; left: 0; top: 395px; width: 340px; height: 85px; background: var(--team-dark); padding: 6px 10px 0; }
  .team__label { font-family: "Marcellus SC", serif; font-size: 10px; color: #fff; text-align: right; }
  .team__label span { color: var(--gold-light); }
  .team__row { display: flex; gap: 6px; margin-top: 6px; }
  .team__portrait { flex: 1; height: 54px; border-bottom: 3px solid var(--navy);
                    background: linear-gradient(180deg, #3a3a42 0%, #55504e 55%, #1c1c22 100%); }

  /* front side */
  .front__photo { position: absolute; left: 0; top: 0; width: 340px; height: 352px; }
  .front__photo--sky { background: linear-gradient(180deg, #8fc3e6 0%, #bcdcef 45%, #7a94b4 80%, #4c5d7a 100%); }
  .front__photo--van { background: linear-gradient(160deg, #5b4337 0%, #b9c9bd 35%, #7b6f66 65%, #3b3531 100%); }
  .front__photo--sunset { background: linear-gradient(160deg, #d6a35e 0%, #a77045 40%, #5c4a3a 75%, #2f3a56 100%); }
  .front .gold-band { top: 352px; }
  .front__claim-panel { position: absolute; left: 0; top: 366px; width: 340px; height: 114px; background: var(--navy);
                        padding: 22px 20px 0 22px; }
  .front__claim { font-family: "Marcellus SC", serif; font-size: 17px; line-height: 1.45; color: #fff; font-weight: 400; }
  .brand { position: absolute; font-family: "Marcellus SC", serif; color: var(--navy); font-size: 22px; letter-spacing: 2px;
           text-align: center; line-height: 1; }
  .brand--on-photo { left: 0; width: 340px; top: 34px; }
  .brand-plate { position: absolute; left: 22px; top: 0; width: 150px; height: 74px; background: #fff;
                 display: flex; align-items: center; justify-content: center; }
  .brand-plate .brand { position: static; font-size: 17px; letter-spacing: 1.5px; }
</style>
</head>
<body>

<!-- pair 1 -->
<section class="flyer-pair flyer-pair--one">
  <article class="flyer back">
    <div class="back__photo" role="img" aria-label="Foto einer modernen weißen Bungalow-Villa mit Garten"></div>
    <div class="gold-band"></div>
    <div class="badge"><span class="badge__top">KOSTENLOSE</span><span class="badge__sub">IMMOBILIEN<br>BEWERTUNG</span></div>
    <div class="back__benefits">
      <h2 class="benefits__title">Das Besondere bei<span>KORVEN Immobilien</span></h2>
      <ul class="benefit-list">
        <li><svg viewBox="0 0 10 10"><path d="M1 5l3 3 5-7" fill="none" stroke="#fff" stroke-width="1.6"/></svg>langjährige Erfahrung mit Immobilien des gehobenen Segments</li>
        <li><svg viewBox="0 0 10 10"><path d="M1 5l3 3 5-7" fill="none" stroke="#fff" stroke-width="1.6"/></svg>hochprofessionelle Komplettabwicklung in kürzester Zeit</li>
        <li><svg viewBox="0 0 10 10"><path d="M1 5l3 3 5-7" fill="none" stroke="#fff" stroke-width="1.6"/></svg>ausgezeichnete Referenzen</li>
        <li><svg viewBox="0 0 10 10"><path d="M1 5l3 3 5-7" fill="none" stroke="#fff" stroke-width="1.6"/></svg>auf Wunsch sehr diskrete Abwicklung</li>
      </ul>
      <p class="benefits__text">Ob Sie eine Immobilie verkaufen oder kaufen möchten, unsere qualifizierten und erfahrenen Makler stehen Ihnen mit ihrem Fachwissen und ihrer persönlichen Beratung zur Seite. Wir sind stets auf dem aktuellen Stand und bieten Ihnen eine individuelle Beratung, damit Sie den bestmöglichen Service erhalten, der auf Ihre spezifischen Anforderungen zugeschnitten ist.</p>
    </div>
    <div class="back__contact">
      <p class="contact__lead">Wenn Sie direkt mit uns sprechen möchten, erreichen Sie uns jederzeit unter</p>
      <p class="contact__phone">0157 - 3948 2036</p>
      <div class="contact__lines">
        <span><svg viewBox="0 0 10 10"><rect x="1" y="2" width="8" height="6" fill="#2b3470"/><path d="M1 2l4 3 4-3" fill="none" stroke="#fff" stroke-width=".8"/></svg>ib@korven-immobilien.example</span>
        <span><svg viewBox="0 0 10 10"><circle cx="5" cy="5" r="4" fill="none" stroke="#2b3470"/><path d="M1 5h8M5 1v8" stroke="#2b3470" stroke-width=".7"/></svg>www.korven-immobilien.example</span>
      </div>
    </div>
    <div class="back__team">
      <p class="team__label">Unser <span>Team</span></p>
      <div class="team__row">
        <div class="team__portrait" role="img" aria-label="Portrait Lorenz Korven"></div>
        <div class="team__portrait" role="img" aria-label="Portrait Teammitglied"></div>
        <div class="team__portrait" role="img" aria-label="Portrait Teammitglied"></div>
        <div class="team__portrait" role="img" aria-label="Portrait Teammitglied"></div>
        <div class="team__portrait" role="img" aria-label="Portrait Henrike Weidlich"></div>
        <div class="team__portrait" role="img" aria-label="Portrait Jonas Weidlich"></div>
      </div>
    </div>
  </article>
  <article class="flyer front">
    <div class="front__photo front__photo--sky" role="img" aria-label="Foto eines lachenden älteren Paares auf einem Motorroller vor blauem Himmel"></div>
    <p class="brand brand--on-photo">KORVEN Immobilien</p>
    <div class="gold-band"></div>
    <div class="front__claim-panel"><p class="front__claim">Genießen Sie Ihre Freiheit.<br>Wir verkaufen Ihre Immobilie.</p></div>
  </article>
</section>

<!-- pair 2 -->
<section class="flyer-pair flyer-pair--two">
  <article class="flyer back">
    <div class="back__photo" role="img" aria-label="Foto einer modernen weißen Bungalow-Villa mit Garten"></div>
    <div class="gold-band"></div>
    <div class="badge"><span class="badge__top">KOSTENLOSE</span><span class="badge__sub">IMMOBILIEN<br>BEWERTUNG</span></div>
    <div class="back__benefits">
      <h2 class="benefits__title">Das Besondere bei<span>KORVEN Immobilien</span></h2>
      <ul class="benefit-list">
        <li><svg viewBox="0 0 10 10"><path d="M1 5l3 3 5-7" fill="none" stroke="#fff" stroke-width="1.6"/></svg>langjährige Erfahrung mit Immobilien des gehobenen Segments</li>
        <li><svg viewBox="0 0 10 10"><path d="M1 5l3 3 5-7" fill="none" stroke="#fff" stroke-width="1.6"/></svg>hochprofessionelle Komplettabwicklung in kürzester Zeit</li>
        <li><svg viewBox="0 0 10 10"><path d="M1 5l3 3 5-7" fill="none" stroke="#fff" stroke-width="1.6"/></svg>ausgezeichnete Referenzen</li>
        <li><svg viewBox="0 0 10 10"><path d="M1 5l3 3 5-7" fill="none" stroke="#fff" stroke-width="1.6"/></svg>auf Wunsch sehr diskrete Abwicklung</li>
      </ul>
      <p class="benefits__text">Ob Sie eine Immobilie verkaufen oder kaufen möchten, unsere qualifizierten und erfahrenen Makler stehen Ihnen mit ihrem Fachwissen und ihrer persönlichen Beratung zur Seite. Wir sind stets auf dem aktuellen Stand und bieten Ihnen eine individuelle Beratung, damit Sie den bestmöglichen Service erhalten, der auf Ihre spezifischen Anforderungen zugeschnitten ist.</p>
    </div>
    <div class="back__contact">
      <p class="contact__lead">Wenn Sie direkt mit uns sprechen möchten, erreichen Sie uns jederzeit unter</p>
      <p class="contact__phone">0157 - 3948 2036</p>
      <div class="contact__lines">
        <span><svg viewBox="0 0 10 10"><rect x="1" y="2" width="8" height="6" fill="#2b3470"/><path d="M1 2l4 3 4-3" fill="none" stroke="#fff" stroke-width=".8"/></svg>ib@korven-immobilien.example</span>
        <span><svg viewBox="0 0 10 10"><circle cx="5" cy="5" r="4" fill="none" stroke="#2b3470"/><path d="M1 5h8M5 1v8" stroke="#2b3470" stroke-width=".7"/></svg>www.korven-immobilien.example</span>
      </div>
    </div>
    <div class="back__team">
      <p class="team__label">Unser <span>Team</span></p>
      <div class="team__row">
        <div class="team__portrait" role="img" aria-label="Portrait Lorenz Korven"></div>
        <div class="team__portrait" role="img" aria-label="Portrait Teammitglied"></div>
        <div class="team__portrait" role="img" aria-label="Portrait Teammitglied"></div>
        <div class="team__portrait" role="img" aria-label="Portrait Teammitglied"></div>
        <div class="team__portrait" role="img" aria-label="Portrait Henrike Weidlich"></div>
        <div class="team__portrait" role="img" aria-label="Portrait Jonas Weidlich"></div>
      </div>
    </div>
  </article>
  <article class="flyer front">
    <div class="front__photo front__photo--van" role="img" aria-label="Foto eines fröhlichen älteren Paares mit Kaffeetassen in der Tür eines Campingbusses"></div>
    <div class="brand-plate"><p class="brand">KORVEN Immobilien</p></div>
    <div class="gold-band"></div>
    <div class="front__claim-panel"><p class="front__claim">Genießen Sie Ihre Freiheit.<br>Wir verkaufen Ihre Immobilie.</p></div>
  </article>
</section>

<!-- pair 3 -->
<section class="flyer-pair flyer-pair--three">
  <article class="flyer back">
    <div class="back__photo" role="img" aria-label="Foto einer modernen weißen Bungalow-Villa mit Garten"></div>
    <div class="gold-band"></div>
    <div class="badge"><span class="badge__top">KOSTENLOSE</span><span class="badge__sub">IMMOBILIEN<br>BEWERTUNG</span></div>
    <div class="back__benefits">
      <h2 class="benefits__title">Das Besondere bei<span>KORVEN Immobilien</span></h2>
      <ul class="benefit-list">
        <li><svg viewBox="0 0 10 10"><path d="M1 5l3 3 5-7" fill="none" stroke="#fff" stroke-width="1.6"/></svg>langjährige Erfahrung mit Immobilien des gehobenen Segments</li>
        <li><svg viewBox="0 0 10 10"><path d="M1 5l3 3 5-7" fill="none" stroke="#fff" stroke-width="1.6"/></svg>hochprofessionelle Komplettabwicklung in kürzester Zeit</li>
        <li><svg viewBox="0 0 10 10"><path d="M1 5l3 3 5-7" fill="none" stroke="#fff" stroke-width="1.6"/></svg>ausgezeichnete Referenzen</li>
        <li><svg viewBox="0 0 10 10"><path d="M1 5l3 3 5-7" fill="none" stroke="#fff" stroke-width="1.6"/></svg>auf Wunsch sehr diskrete Abwicklung</li>
      </ul>
      <p class="benefits__text">Ob Sie eine Immobilie verkaufen oder kaufen möchten, unsere qualifizierten und erfahrenen Makler stehen Ihnen mit ihrem Fachwissen und ihrer persönlichen Beratung zur Seite. Wir sind stets auf dem aktuellen Stand und bieten Ihnen eine individuelle Beratung, damit Sie den bestmöglichen Service erhalten, der auf Ihre spezifischen Anforderungen zugeschnitten ist.</p>
    </div>
    <div class="back__contact">
      <p class="contact__lead">Wenn Sie direkt mit uns sprechen möchten, erreichen Sie uns jederzeit unter</p>
      <p class="contact__phone">0157 - 3948 2036</p>
      <div class="contact__lines">
        <span><svg viewBox="0 0 10 10"><rect x="1" y="2" width="8" height="6" fill="#2b3470"/><path d="M1 2l4 3 4-3" fill="none" stroke="#fff" stroke-width=".8"/></svg>ib@korven-immobilien.example</span>
        <span><svg viewBox="0 0 10 10"><circle cx="5" cy="5" r="4" fill="none" stroke="#2b3470"/><path d="M1 5h8M5 1v8" stroke="#2b3470" stroke-width=".7"/></svg>www.korven-immobilien.example</span>
      </div>
    </div>
    <div class="back__team">
      <p class="team__label">Unser <span>Team</span></p>
      <div class="team__row">
        <div class="team__portrait" role="img" aria-label="Portrait Lorenz Korven"></div>
        <div class="team__portrait" role="img" aria-label="Portrait Teammitglied"></div>
        <div class="team__portrait" role="img" aria-label="Portrait Teammitglied"></div>
        <div class="team__portrait" role="img" aria-label="Portrait Teammitglied"></div>
        <div class="team__portrait" role="img" aria-label="Portrait Henrike Weidlich"></div>
        <div class="team__portrait" role="img" aria-label="Portrait Jonas Weidlich"></div>
      </div>
    </div>
  </article>
  <article class="flyer front">
    <div class="front__photo front__photo--sunset" role="img" aria-label="Foto eines jubelnden jungen Paares auf einem Motorroller im warmen Abendlicht"></div>
    <div class="brand-plate"><p class="brand">KORVEN Immobilien</p></div>
    <div class="gold-band"></div>
    <div class="front__claim-panel"><p class="front__claim">Genießen Sie Ihre Freiheit.<br>Wir verkaufen Ihre Immobilie.</p></div>
  </article>
</section>

</body>
</html>
```